The Hidden Roots of Lingering Illness Decoded

Subtitle: At last, uncover what drives your aches, exhaustion, and swelling.

I need an awesome book cover that fits this title.

```html
<!DOCTYPE html>
<html lang="en">
<head>
<meta charset="utf-8">
<title>The Hidden Roots of Lingering Illness Decoded</title>
<link href="https://fonts.googleapis.com/css2?family=Montserrat:wght@500;600;800&display=swap" rel="stylesheet">
<style>
  :root {
    --ink-deep: #04303c;
    --ink-mid: #0b3340;
    --glow-plum: #4a2f3a;
    --accent-red: #e04b3c;
    --title-white: #ffffff;
    --subtitle-white: #e8e6e3;
    --pulse-grey: #6f7f86;
  }
  * { margin: 0; padding: 0; box-sizing: border-box; }
  html, body { width: 800px; height: 1200px; overflow: hidden; background: var(--ink-deep); }
  .cover {
    position: relative;
    width: 800px;
    height: 1200px;
    overflow: hidden;
    background:
      radial-gradient(ellipse 360px 380px at 50% 62%, rgba(92, 48, 60, 0.75), rgba(40, 44, 60, 0.35) 60%, rgba(4, 48, 60, 0) 100%),
      linear-gradient(180deg, var(--ink-deep) 0%, var(--ink-mid) 50%, var(--ink-deep) 100%);
    font-family: "Montserrat", sans-serif;
  }
  .title {
    position: absolute;
    top: 78px;
    left: 0;
    width: 100%;
    text-align: center;
    font-weight: 800;
    text-transform: uppercase;
    color: var(--title-white);
    line-height: 78px;
  }
  .title-line { display: block; white-space: nowrap; letter-spacing: 0.14em; padding-left: 0.14em; }
  .title-line--lead { font-size: 68px; }
  .title-line--accent { font-size: 60px; color: var(--accent-red); }
  .title-line--mid { font-size: 58px; }
  .title-line--tail { font-size: 66px; }
  .pulse-line {
    position: absolute;
    left: 0;
    top: 720px;
    width: 800px;
    height: 110px;
  }
  .illustration {
    position: absolute;
    left: 170px;
    top: 505px;
    width: 470px;
    height: 440px;
    border-radius: 48% 52% 45% 55% / 42% 45% 55% 58%;
    background: radial-gradient(ellipse at 50% 55%, #d9503f 0%, #a5433f 28%, #4a2f3a 62%, rgba(30, 40, 55, 0) 100%);
  }
  .subtitle {
    position: absolute;
    top: 1018px;
    left: 0;
    width: 100%;
    text-align: center;
    font-weight: 600;
    font-size: 29px;
    line-height: 42px;
    letter-spacing: 0.12em;
    text-transform: uppercase;
    color: var(--subtitle-white);
  }
  .subtitle-line { display: block; white-space: nowrap; }
  .subtitle-accent { color: var(--accent-red); }
</style>
</head>
<body>
  <main class="cover">
    <h1 class="title">
      <span class="title-line title-line--lead">The</span>
      <span class="title-line title-line--accent">Hidden Roots</span>
      <span class="title-line title-line--mid">of Lingering</span>
      <span class="title-line title-line--lead">Illness</span>
      <span class="title-line title-line--tail">Decoded</span>
    </h1>

    <svg class="pulse-line" viewBox="0 0 800 110" aria-hidden="true">
      <polyline fill="none" stroke="var(--pulse-grey)" stroke-width="1.2"
        points="5,47 55,47 60,42 67,52 80,41 93,62 120,10 143,95 170,26 184,52 196,40 253,47"/>
      <polyline fill="none" stroke="var(--pulse-grey)" stroke-width="1.2"
        points="547,47 604,47 610,40 622,52 637,26 664,95 687,10 714,62 727,41 740,52 747,42 752,47 800,47"/>
    </svg>

    <div class="illustration" role="img" aria-label="Illustration of a woman in a red top holding her hands up in distress, surrounded by pink burst marks, a heartbeat heart, a stethoscope and question marks"></div>

    <p class="subtitle">
      <span class="subtitle-line"><span class="subtitle-accent">At last,</span> uncover what</span>
      <span class="subtitle-line">drives your aches, exhaustion,</span>
      <span class="subtitle-line">and swelling.</span>
    </p>
  </main>
</body>
</html>
```